Website for Cedar Brook Fellowship Church

Wordpress website design required for Cedar Brook Fellowship Church. We are a family oriented church catering for age groups from school age to elderly people. The church has a wide variety of activities which it coordinates. The idea is to describe the activities on the activities page, but cross-link them to show which would be applicable to the different age groups.

We would like an inviting website which is easy to read and navigate.

Target Market(s)

Very wide audience - from school age youth to elderly people, so design and style should cater for both audiences.

Industry/Entity Type

Church

Coding

Coded - Design and coding required

Number of Pages Required

5+ page

Font styles to use
Sans Serif

Colors
0255a3
ffffff
0792cd
f78f20

Requirements
Must have
• Inviting website.
• Clear readable font.
• Space to import photos to balance text on each page.
• Need to project a dynamic and progressive feel for the church.
• Easy to navigate.
Nice to have
• Scrolling photos on pages. Ability to enter questions/ comments/prayer requests on Home page.
Should not have
• Conservative audience, so should not be too bold.

```html
<!DOCTYPE html>
<html lang="en">
<head>
<meta charset="utf-8">
<title>Cedar Brook Fellowship Church</title>
<link rel="stylesheet" href="https://fonts.googleapis.com/css2?family=Open+Sans:ital,wght@0,400;0,600;0,700;1,400;1,600&family=Dancing+Script:wght@700&family=Crimson+Text:ital@1&display=swap">
<style>
:root{
  --blue:#0255a3;
  --navy:#12489a;
  --sky:#0792cd;
  --panel:#1a7cc8;
  --orange:#f78f20;
  --white:#ffffff;
  --paper:#eef0f1;
  --grey:#e5e6e7;
  --ink:#333a44;
}
*{margin:0;padding:0;box-sizing:border-box}
html,body{width:907px;height:1200px;overflow:hidden}
body{position:relative;background:var(--paper);font-family:"Open Sans",Arial,sans-serif;color:var(--ink)}
.abs{position:absolute}
.header{left:0;top:0;width:907px;height:103px;background:var(--white)}
.brand{left:122px;top:46px;display:flex;align-items:center;gap:6px;font-size:14px;font-weight:600;color:#4a4f57}
.brand-dot{width:9px;height:9px;border-radius:50%;background:var(--navy)}
.partner{left:724px;top:16px;width:60px;height:60px;border-radius:50%;border:3px solid #1b1b1b;display:flex;align-items:center;justify-content:center;font-size:7px;font-weight:600;color:#1b1b1b;text-align:center;line-height:1.2;background:var(--white)}
.nav{left:122px;top:90px;width:663px;height:36px;background:linear-gradient(#1a6fc4,#0a4a9c);display:flex;align-items:center;padding-left:26px;gap:17px}
.nav a{color:var(--white);font-size:8.5px;text-decoration:none;text-transform:uppercase}
.search{left:751px;top:94px;width:30px;height:24px;background:var(--orange);display:flex;align-items:center;justify-content:center}
.slider{left:122px;top:131px;width:663px;height:272px;background:var(--white);box-shadow:0 1px 4px rgba(0,0,0,.3)}
.slide-photo{left:4px;top:5px;width:480px;height:263px;background:linear-gradient(160deg,#6fa6dc 0%,#d9d2c2 40%,#3d3b38 70%,#c9b487 100%)}
.slide-panel{left:4px;top:5px;width:655px;height:263px}
.welcome{left:416px;top:50px;width:200px;color:var(--white)}
.welcome h1{font-size:22px;font-weight:700;letter-spacing:.3px;margin-bottom:8px}
.welcome p{font-size:8px;line-height:16px;text-align:justify}
.btn{background:var(--orange);color:var(--white);font-weight:600;display:flex;align-items:center;justify-content:center}
.learn{left:416px;top:194px;width:85px;height:24px;font-size:10px;border-radius:2px}
.dots{left:590px;top:246px;display:flex;gap:5px}
.dots span{width:7px;height:7px;border-radius:50%;background:var(--white)}
.dots span.ring{background:transparent;border:1.5px solid var(--white)}
.section-title{font-size:15px;font-weight:700;color:var(--navy)}
.grid{left:122px;top:442px;width:663px;height:236px;display:grid;grid-template-columns:repeat(4,1fr);grid-template-rows:repeat(2,1fr);gap:1px}
.grid .cell{position:relative}
.activity-card{background:var(--navy);color:var(--white);padding:16px 14px}
.activity-card h3{font-size:11px;font-weight:700;margin-bottom:6px}
.activity-card p{font-size:7.2px;line-height:16px}
.activity-card::before{content:"";position:absolute;left:-6px;top:52px;border:6px solid transparent;border-right-color:var(--navy);border-left:0}
.message{left:170px;top:697px;width:567px;height:57px;background:var(--orange);border-radius:2px;display:flex;align-items:center;padding:0 32px}
.message h4{font-family:"Dancing Script",cursive;font-size:19px;color:var(--white);width:103px;flex:none}
.message p{font-family:"Crimson Text",Georgia,serif;font-style:italic;color:var(--white);font-size:10.5px;line-height:16px;text-align:justify}
.news{top:812px;width:215px;height:148px}
.news-overlay{left:0;top:49px;width:215px;height:99px;background:rgba(2,60,150,.88);color:var(--white);padding:8px 21px}
.news-overlay .date{font-size:7px;font-weight:700;margin-bottom:4px}
.news-overlay h3{font-size:12.5px;font-weight:600;line-height:16px;margin-bottom:4px}
.news-overlay p{font-size:7px;font-style:italic;line-height:16px}
.prayer{left:570px;background:var(--grey);padding:24px 25px}
.prayer h3{font-size:15px;font-weight:600;color:var(--navy);margin-bottom:5px}
.prayer p{font-size:9px;font-style:italic;line-height:16px;color:#555}
.prayer .btn{width:146px;height:20px;font-size:8px;margin-top:13px}
.footer{left:0;top:980px;width:907px;height:186px;background:linear-gradient(180deg,#0a3f9c,#0c4aa6)}
.footer h4{font-size:14px;font-weight:600;color:var(--white)}
.foot-item{display:flex;gap:9px;font-size:7.5px;color:var(--white);line-height:16px}
.foot-item svg{flex:none;margin-top:3px}
.input{left:350px;top:1026px;width:146px;height:19px;background:var(--white);font-size:8px;color:#888;padding:3px 12px;font-weight:600}
.send{left:350px;top:1052px;width:146px;height:19px;font-size:8px;border-radius:1px}
.theme-text{left:580px;top:1024px;width:186px;font-size:7.2px;font-style:italic;color:var(--white);line-height:15px;text-align:justify}
.like-box{left:654px;top:1094px;width:22px;height:22px;background:var(--white);border-radius:2px}
.bottom-bar{left:0;top:1166px;width:907px;height:34px;background:#1a6dc2;color:var(--white);font-size:7px;display:flex;align-items:center;justify-content:center}
</style>
</head>
<body>
<header class="abs header"></header>
<div class="abs brand"><span class="brand-dot"></span>Cedar Brook Fellowship Church</div>
<div class="abs partner">Harbor<br>Union</div>

<nav class="abs nav">
  <a>Home</a><a>Age Group</a><a>Activities</a><a>Events Calendar</a><a>About</a><a>Contact</a>
</nav>
<div class="abs search">
  <svg width="10" height="10" viewBox="0 0 10 10"><circle cx="4" cy="4" r="3" fill="none" stroke="#fff" stroke-width="1.4"/><line x1="6.2" y1="6.2" x2="9" y2="9" stroke="#fff" stroke-width="1.6"/></svg>
</div>

<section class="abs slider">
  <div class="abs slide-photo" role="img" aria-label="Church building with its welcome sign under a blue sky"></div>
  <svg class="abs slide-panel" viewBox="0 0 655 263" width="655" height="263">
    <polygon points="478,0 655,0 655,263 480,263 416,140" fill="#1a7cc8"/>
  </svg>
  <div class="abs welcome">
    <h1>WELCOME !</h1>
    <p>Et harum quidem rerum facilis est et expedita distinctio. Nam libero tempore, cum soluta nobis est eligendi optio cumque nihil impedit quo minus id quod maxime placeat facere possimus, omnis voluptas assumenda est, omnis dolor repellendus. Temporibus autem quibusdam et aut officiis</p>
  </div>
  <div class="abs btn learn">Learn More</div>
  <div class="abs dots"><span></span><span class="ring"></span><span></span><span></span></div>
</section>

<h2 class="abs section-title" style="left:122px;top:414px">OUR ACTIVITIES</h2>
<div class="abs grid">
  <div class="cell" role="img" aria-label="Members sharing a buffet lunch" style="background:linear-gradient(135deg,#8a6a55,#c9a27a,#5e4a3f)"></div>
  <div class="cell activity-card">
    <h3>ACTIVITY NAME</h3>
    <p>Nam libero tempore, cum soluta nobis est eligendi optio cumque nihil impedit quo minus id quod maxime placeat facere possimus, omnis voluptas</p>
  </div>
  <div class="cell" role="img" aria-label="Celebration with birthday cakes in the hall" style="background:linear-gradient(135deg,#6e6a66,#b9b2a8,#3c3a3a)"></div>
  <div class="cell" role="img" aria-label="Family group smiling together" style="background:linear-gradient(135deg,#3f3a38,#c79a80,#2c3f7a)"></div>
  <div class="cell" role="img" aria-label="Church member at a gathering" style="background:linear-gradient(135deg,#6a5040,#d1b49e,#2d2a2a)"></div>
  <div class="cell" role="img" aria-label="Couple at a church evening" style="background:linear-gradient(135deg,#4b3f4a,#b88fa0,#2f3c55)"></div>
  <div class="cell" role="img" aria-label="Church tower against a blue sky" style="background:linear-gradient(180deg,#3f79c7,#9bb7dc 40%,#b89a5a 60%,#4a4030)"></div>
  <div class="cell" role="img" aria-label="Two young members smiling" style="background:linear-gradient(135deg,#2e2624,#c79a86,#3b2c2a)"></div>
</div>

<div class="abs message">
  <h4>Message</h4>
  <p>“ Nemo enim ipsam voluptatem quia voluptas sit aspernatur aut odit aut fugit, sed quia consequuntur magni dolores eos qui ratione voluptatem sequi nesciunt.”</p>
</div>

<h2 class="abs section-title" style="left:127px;top:776px">NEWS</h2>
<article class="abs news" style="left:122px;background:linear-gradient(135deg,#5a2e22,#c8846a,#3a2a26)" role="img" aria-label="Member portrait for news story">
  <div class="abs news-overlay">
    <div class="date">Date : 12-10-2016</div>
    <h3>What's wrong with a little sledging?</h3>
    <p>Duis aute irure dolor in reprehenderit in voluptate velit esse cillum dolore eu fugiat nulla pariatur.</p>
  </div>
</article>
<div class="abs news" style="left:346px;background:linear-gradient(135deg,#5a3a22,#b8935a,#3c4a5a)" role="img" aria-label="Couple smiling at a church event"></div>
<aside class="abs news prayer">
  <h3>PRAYER REQUEST</h3>
  <p>Duis aute irure dolor in reprehenderit in voluptate velit esse cillum dolore eu fugiat nulla pariatur.</p>
  <div class="btn">prayers@cedarbrookchurch.org</div>
</aside>

<footer class="abs footer"></footer>
<h4 class="abs" style="left:142px;top:997px;font-size:14px;font-weight:600;color:#fff">Contact Details</h4>
<div class="abs foot-item" style="left:142px;top:1035px">
  <svg width="6" height="8" viewBox="0 0 6 8"><path d="M3 0a3 3 0 0 1 3 3c0 2-3 5-3 5S0 5 0 3a3 3 0 0 1 3-3z" fill="#8fb0e0"/></svg>
  <span>Brookside Ministries Ltd.<br>18, Willow Lane, Maple Ridge<br>MR 20417</span>
</div>
<div class="abs foot-item" style="left:142px;top:1098px">
  <svg width="6" height="9" viewBox="0 0 6 9"><rect x=".5" y=".5" width="5" height="8" rx="1" fill="none" stroke="#8fb0e0"/></svg>
  <span>(555) 014 27 63</span>
</div>
<div class="abs foot-item" style="left:142px;top:1130px">
  <svg width="8" height="6" viewBox="0 0 8 6"><rect x=".5" y=".5" width="7" height="5" fill="none" stroke="#8fb0e0"/><path d="M.5 .5L4 3.5 7.5 .5" fill="none" stroke="#8fb0e0"/></svg>
  <span>hello@cedarbrookchurch.org</span>
</div>

<h4 class="abs" style="left:350px;top:997px;font-size:14px;font-weight:600;color:#fff">Join Our Email</h4>
<div class="abs input">Enter your Email id</div>
<div class="abs btn send">Send Email</div>
<h4 class="abs" style="left:350px;top:1080px;font-size:14px;font-weight:600;color:#fff">Service Times</h4>
<div class="abs foot-item" style="left:352px;top:1107px;font-size:8.5px">
  <svg width="8" height="8" viewBox="0 0 8 8"><circle cx="4" cy="4" r="3.2" fill="none" stroke="#fff" stroke-width="1.2"/><path d="M4 2v2h1.5" stroke="#fff" fill="none"/></svg>
  <span>Morning 9:00 am to 8:00 pm</span>
</div>

<h4 class="abs" style="left:578px;top:997px;font-size:14px;font-weight:600;color:#fff">Theme of Church</h4>
<p class="abs theme-text">Duis aute irure dolor in reprehenderit in voluptate velit esse cillum dolore eu fugiat nulla pariatur. Excepteur sint occaecat cupidatat non proident, sunt in culpa qui officia deserunt mollit anim id est laborum</p>
<h4 class="abs" style="left:579px;top:1094px;font-size:14px;font-weight:600;color:#fff">Follow Us</h4>
<div class="abs like-box"></div>
<div class="abs" style="left:682px;top:1100px;font-size:8px;color:#fff">Like our page</div>

<div class="abs bottom-bar">Copyright © 2016 www.cedarbrookchurch.org &nbsp;All Rights Reserved.</div>
</body>
</html>
```